Professional On-line Wine Education Course Poster

I need a sales poster to draw potential students to an on-line course for professional wine training and certification. My business is The Vine Loft (www.thevineloft.example).
We are an approved provider for the international credential for The Grape and Barrel Guild in London, England. My company is located in Arkansas and serves other markets in the southeastern United States.
It is a unique opportunity for students. The classroom is supported by teachers in London so anywhere ... anytime they can participate in the course. The student may be in Arkansas or surrounding states but may have other students participating in China, Paris, California.
The GBGO Certification is unique and recognized around the world as the premier wine education program.
The posters main purpose is to draw attention to the student enough to have them call or visit the web site for more information. It needs to be eye catching and appealing to a younger market (Under 30). They will be hanging on college campuses, culinary schools, large hotels and restaurants in the employee lounge and possibly wine shops. Because they may be in service or hospitality or even enology or viticulture the main thoughts on images don't need to be just chefs. VERY important is the fact this is on-line with no classroom. Students attend when it's convenient for them.
Pursue wine certifications on line
Differentiate yourself!
Fast-track your career!
Learn from the world leader in wine education
Affordable ... dynamic ... learn at your own pace
Increase your knowledge and income potential
I have also attached brand guidelines from GBGO that might help drive look and feel, a brochure from GBGO that has additional content about the programs and several logos from GBGO and The Vine Loft which is an Approved Program Provider for GBGO.
High impact photos are welcome. Please incorporate photos that you think help increase appeal. We can purchase photos separately upon successful selection of the project.
Reason: We have updated the requirements and increased the budget to drive additional submissions.
Target Market(s)
Less is more on this project. Looking for high impact visual to get potential students to visit website (TheVineLoft.example) or call the number (855.271.6094). Online wine education with a certification that is recognized globally. These credentials increase a candidates marketability for work in hospitality, restaurant management & entertainment venues.
Industry/Entity Type
Hospitality
Look and feel

```html
<!DOCTYPE html>
<html lang="en">
<head>
<meta charset="utf-8">
<title>Online Wine Education – The Vine Loft</title>
<link rel="stylesheet" href="https://fonts.googleapis.com/css2?family=Archivo+Black&family=Raleway:wght@100;200&family=Montserrat:ital,wght@0,200;0,300;0,500;0,700;0,800;1,400;1,800&display=swap">
<style>
  :root {
    --ink: #0d0d0d;
    --grape: #5b2f86;
    --grape-soft: #7a55a0;
    --paper: #ffffff;
  }
  html, body {
    margin: 0;
    padding: 0;
    overflow: hidden;
    background: var(--paper);
  }
  .poster {
    display: block;
    width: 776px;
    height: 1200px;
    background: var(--paper);
  }
  .headline-online { font-family: "Archivo Black", "Arial Black", sans-serif; fill: var(--ink); }
  .headline-wine { font-family: "Raleway", "Helvetica Neue", sans-serif; font-weight: 100; fill: var(--ink); }
  .headline-education { font-family: "Raleway", "Helvetica Neue", sans-serif; font-weight: 200; fill: var(--ink); }
  .line-thin { font-family: "Montserrat", Arial, sans-serif; font-weight: 200; fill: var(--ink); }
  .line-leader { font-family: "Montserrat", Arial, sans-serif; font-weight: 800; font-style: italic; fill: var(--grape); }
  .line-bold { font-family: "Montserrat", Arial, sans-serif; font-weight: 700; fill: var(--ink); }
  .line-italic { font-family: "Montserrat", Arial, sans-serif; font-weight: 400; font-style: italic; fill: var(--ink); }
  .line-cert { font-family: "Montserrat", Arial, sans-serif; font-weight: 200; fill: var(--grape); }
  .visit { font-family: "Montserrat", Arial, sans-serif; font-weight: 800; fill: var(--ink); }
  .brand-name { font-family: "Montserrat", Arial, sans-serif; font-weight: 500; fill: var(--grape); }
  .accent { fill: var(--grape); }
  .badge { fill: none; stroke: var(--ink); stroke-width: 2; }
</style>
</head>
<body>
<svg class="poster" viewBox="0 0 776 1200" xmlns="http://www.w3.org/2000/svg">

  <!-- Headline: ONLINE -->
  <g class="headline">
    <ellipse class="accent" cx="132" cy="83" rx="54" ry="50"/>
    <text class="headline-online" x="190" y="131" font-size="132" textLength="506" lengthAdjust="spacingAndGlyphs">NLINE</text>

    <!-- WINE, with a bottle standing in for the I -->
    <text class="headline-wine" x="80" y="333" font-size="250" textLength="232" lengthAdjust="spacingAndGlyphs">W</text>
    <rect class="accent" x="322" y="148" width="62" height="186" rx="10"
          role="img" aria-label="Wine bottle silhouette forming the letter I"/>
    <text class="headline-wine" x="398" y="333" font-size="250" textLength="156" lengthAdjust="spacingAndGlyphs">N</text>
    <text class="headline-wine" x="570" y="333" font-size="250" textLength="128" lengthAdjust="spacingAndGlyphs">E</text>

    <!-- EDUCATION, with a solid disc for the O -->
    <text class="headline-education" x="94" y="398" font-size="74" textLength="455" lengthAdjust="spacingAndGlyphs">EDUCATI</text>
    <circle class="accent" cx="588" cy="370" r="33"/>
    <text class="headline-education" x="627" y="398" font-size="74" textLength="78" lengthAdjust="spacingAndGlyphs">N</text>

    <rect x="352" y="404" width="180" height="90" rx="30" fill="var(--grape-soft)" opacity="0.85"
          role="img" aria-label="Bottle neck trailing into a computer mouse cable and mouse"/>
  </g>

  <!-- Message block -->
  <g class="message">
    <text class="line-thin" x="94" y="572" font-size="50" textLength="611" lengthAdjust="spacingAndGlyphs">LEARN FROM THE</text>
    <text class="line-leader" x="110" y="642" font-size="64" textLength="596" lengthAdjust="spacingAndGlyphs">WORLD LEADER</text>
    <text class="line-bold" x="98" y="703" font-size="56" textLength="607" lengthAdjust="spacingAndGlyphs">IN WINE EDUCATION</text>
    <text class="line-italic" x="96" y="757" font-size="50" textLength="610" lengthAdjust="spacingAndGlyphs">&amp; GET A GLOBALLY</text>
    <text class="line-cert" x="98" y="804" font-size="44" textLength="607" lengthAdjust="spacingAndGlyphs">RECOGNIZED CERTIFICATION</text>
  </g>

  <!-- Call to action -->
  <text class="visit" x="110" y="992" font-size="34" textLength="595" lengthAdjust="spacingAndGlyphs">VISIT www.TheVineLoft.example</text>

  <!-- Sign-off -->
  <g class="signoff">
    <text class="brand-name" x="148" y="1118" font-size="38">The Vine Loft</text>
    <rect class="badge" x="472" y="1055" width="162" height="108" rx="4"
          role="img" aria-label="Approved programme provider badge"/>
  </g>
</svg>
</body>
</html>
```